Business Card Design Project

This is a new division in our company. "Meridale Wellsite & Safety" This is a Oilfield Safety company. I have included our new logo. I also have given our other business card. We love double sided with lots of color. We like to stand out. Please DO NOT duplicate our other card and bring your design into it. See all attached files.
Reason: forgot to change this when I posted it.
Here is the correct information card.
www.meridalewellsitesafety.com
Dwayne@meridalewellsitesafety.com
Reason: revision for a few.
Reason: was traveling and need to review designs.
Oil and Gas industry. Masculine look.
Business

```html
<!DOCTYPE html>
<html lang="en">
<head>
<meta charset="utf-8">
<title>Meridale Wellsite &amp; Safety — Business Card</title>
<link rel="stylesheet" href="https://fonts.googleapis.com/css2?family=Michroma&family=Didact+Gothic&display=swap">
<style>
  :root {
    --page: #d6d6d6;
    --card-grey: #a3a29e;
    --card-white: #f7f7f5;
    --yellow: #d8d52b;
    --teal: #4cc0bf;
    --teal-light: #7fd3d1;
    --red: #e1262b;
    --orange: #f0a23a;
    --orange-red: #e5542b;
    --green: #35a853;
    --ink: #262626;
  }
  * { margin: 0; padding: 0; box-sizing: border-box; }
  html, body { width: 1200px; height: 1000px; overflow: hidden; }
  body {
    background: radial-gradient(ellipse at 50% 20%, #f2f2f2 0%, var(--page) 70%);
    position: relative;
    font-family: "Didact Gothic", "Century Gothic", sans-serif;
  }
  .card {
    position: absolute;
    left: 290px;
    width: 620px;
    height: 354px;
    overflow: hidden;
    box-shadow: 0 6px 18px rgba(0,0,0,0.18);
  }
  .card-back { top: 90px; }
  .card-front { top: 530px; }
  .card-art { position: absolute; inset: 0; width: 100%; height: 100%; }

  .brand {
    position: absolute;
    display: flex;
    align-items: center;
    gap: 10px;
    font-family: "Michroma", sans-serif;
    color: var(--teal);
    line-height: 1.15;
  }
  .brand-mark { width: 18px; height: 18px; background: var(--orange-red); flex: none; }
  .card-back .brand { left: 90px; top: 128px; font-size: 22px; width: 330px; }
  .card-front .brand { left: 22px; top: 26px; font-size: 15px; width: 260px; }

  .contact-lines {
    position: absolute;
    left: 382px; top: 46px;
    font-size: 15px;
    color: var(--ink);
    line-height: 1.3;
    letter-spacing: 0.5px;
  }
  .holder {
    position: absolute;
    left: 150px; top: 134px;
    width: 450px;
  }
  .holder-name {
    font-family: "Michroma", sans-serif;
    font-weight: 400;
    color: var(--red);
    font-size: 21px;
    line-height: 1.3;
    letter-spacing: 1px;
    -webkit-text-stroke: 0.6px var(--red);
  }
  .holder-email {
    font-size: 14px;
    color: #ffffff;
    letter-spacing: 0.4px;
    margin-top: 4px;
  }
  .address-lines {
    position: absolute;
    left: 180px; top: 240px;
    font-size: 15px;
    color: var(--ink);
    line-height: 1.3;
    letter-spacing: 0.5px;
  }
</style>
</head>
<body>

  <section class="card card-back" aria-label="Card back">
    <svg class="card-art" viewBox="0 0 620 354" aria-hidden="true">
      <rect width="620" height="354" fill="var(--card-white)"/>
      <polyline points="430,-4 582,177 430,358" fill="none" stroke="var(--teal)" stroke-width="9"/>
      <polyline points="420,-4 572,177 420,358" fill="none" stroke="var(--green)" stroke-width="9"/>
      <polyline points="410,-4 562,177 410,358" fill="none" stroke="var(--orange-red)" stroke-width="9"/>
      <polygon points="0,0 408,0 558,177 408,354 0,354" fill="var(--card-grey)"/>
    </svg>
    <div class="brand"><span class="brand-mark"></span><span class="brand-name">Meridale Wellsite &amp; Safety</span></div>
  </section>

  <section class="card card-front" aria-label="Card front">
    <svg class="card-art" viewBox="0 0 620 354" aria-hidden="true">
      <defs>
        <linearGradient id="band-shade" x1="0" y1="0" x2="0" y2="1">
          <stop offset="0" stop-color="var(--teal)"/>
          <stop offset="0.5" stop-color="var(--teal-light)"/>
          <stop offset="1" stop-color="var(--teal)"/>
        </linearGradient>
      </defs>
      <rect width="620" height="354" fill="var(--card-grey)"/>
      <polygon points="0,0 415,0 0,305" fill="var(--yellow)"/>
      <rect x="0" y="122" width="620" height="80" fill="url(#band-shade)"/>
      <polygon points="620,262 620,276 510,354 488,354" fill="var(--red)"/>
      <polygon points="620,282 620,354 518,354" fill="var(--orange)"/>
    </svg>
    <div class="brand"><span class="brand-mark"></span><span class="brand-name">Meridale Wellsite &amp; Safety</span></div>
    <div class="contact-lines">
      <p>Fax: 1-888-555-0147</p>
      <p>Office: 201 - 555 0183</p>
      <p>Cell: 713-555-0126</p>
    </div>
    <div class="holder">
      <p class="holder-name">Dwayne Halvorsen</p>
      <p class="holder-email">Email: Dwayne@meridalewellsitesafety.com</p>
    </div>
    <div class="address-lines">
      <p>4820 N. Calloway, TX 77301</p>
      <p>www.meridalewellsitesafety.com</p>
    </div>
  </section>

</body>
</html>
```